Medical Aesthetics business cards

Looking for a business card for my new medical aesthetics business. I am a nurse practitioner and will be administering dravine , fillers as well as providing other services

```html
<!DOCTYPE html>
<html lang="en">
<head>
<meta charset="utf-8">
<title>Clara Vance – Business Card</title>
<link href="https://fonts.googleapis.com/css2?family=Lato:wght@300;400;700&display=swap" rel="stylesheet">
<style>
  :root {
    --page-bg: #ece9e4;
    --card-white: #ffffff;
    --plum: #a4346d;
    --sand: #e2b898;
    --ink: #2b2b2b;
    --photo-light: #f3ddd0;
    --photo-mid: #e3b9a3;
    --photo-dark: #c99682;
  }
  * { margin: 0; padding: 0; box-sizing: border-box; }
  html, body {
    width: 1200px; height: 1159px; overflow: hidden;
    background: var(--page-bg);
    font-family: "Lato", sans-serif;
  }
  .business-card {
    position: absolute;
    left: 50px; top: 265px;
    width: 1100px; height: 629px;
    border-radius: 32px;
    overflow: hidden;
    background: var(--card-white);
  }
  .portrait-photo {
    position: absolute;
    left: 0; top: 0;
    width: 640px; height: 560px;
    background:
      radial-gradient(ellipse 60% 70% at 45% 40%, var(--photo-light) 0%, var(--photo-mid) 55%, rgba(227,185,163,0) 100%),
      linear-gradient(90deg, var(--photo-mid) 0%, var(--photo-light) 70%, rgba(255,255,255,0) 100%);
  }
  .wave-bands {
    position: absolute; left: 0; top: 0;
    width: 1100px; height: 629px;
  }
  .practitioner {
    position: absolute;
    right: 40px; top: 200px;
    text-align: right;
  }
  .practitioner-name {
    color: var(--plum);
    font-weight: 400;
    font-size: 41px;
    line-height: 1;
    letter-spacing: 0.3px;
  }
  .practitioner-name .credential { font-size: 33px; }
  .practitioner-title {
    margin-top: 12px;
    color: var(--ink);
    font-weight: 400;
    font-size: 24px;
    letter-spacing: 1px;
  }
  .services {
    position: absolute;
    left: 39px; top: 566px;
    color: #fff;
    font-weight: 700;
    font-size: 26px;
    letter-spacing: 0.2px;
  }
  .services .divider { margin: 0 14px; font-weight: 400; }
  .contact-list {
    position: absolute;
    right: 40px; top: 494px;
    list-style: none;
    text-align: right;
    color: #fff;
    font-weight: 300;
    font-size: 25px;
    letter-spacing: 0.6px;
  }
  .contact-list li {
    display: flex; justify-content: flex-end; align-items: center;
    height: 35px;
  }
  .contact-list svg { margin-left: 16px; width: 23px; height: 23px; }
</style>
</head>
<body>
  <div class="business-card">
    <div class="portrait-photo" role="img" aria-label="Photo of a woman's lower face and neck receiving a cosmetic injection from a gloved hand"></div>

    <svg class="wave-bands" viewBox="0 0 1346 770" preserveAspectRatio="none" aria-hidden="true">
      <path fill="var(--sand)" d="M0,500 C190,612 430,632 660,560 C820,510 940,448 1050,436 L1346,436 L1346,770 L0,770Z"/>
      <path fill="var(--card-white)" d="M0,578 C200,684 450,686 700,594 C880,528 1000,446 1100,440 L1346,440 L1346,770 L0,770Z"/>
      <path fill="var(--plum)" d="M0,598 C200,702 450,702 700,612 C880,542 1000,460 1100,460 C1200,460 1290,500 1346,540 L1346,770 L0,770Z"/>
    </svg>

    <div class="practitioner">
      <h1 class="practitioner-name">Clara Vance, <span class="credential">APRN-C</span></h1>
      <p class="practitioner-title">Nurse Practitioner</p>
    </div>

    <p class="services">Offering: dravine<span class="divider">|</span>fillers<span class="divider">|</span>lumaline</p>

    <ul class="contact-list">
      <li>555-014-2290
        <svg viewBox="0 0 24 24" fill="#fff"><path d="M6.6 10.8a15.1 15.1 0 0 0 6.6 6.6l2.2-2.2a1 1 0 0 1 1-.25 11.4 11.4 0 0 0 3.6.57 1 1 0 0 1 1 1V20a1 1 0 0 1-1 1A17 17 0 0 1 3 4a1 1 0 0 1 1-1h3.5a1 1 0 0 1 1 1c0 1.25.2 2.45.57 3.57a1 1 0 0 1-.25 1z" transform="rotate(180 12 12) scale(-1 1) translate(-24 0)"/></svg>
      </li>
      <li>hello@glowformstudio.com
        <svg viewBox="0 0 24 24" fill="#fff"><rect x="2" y="5" width="20" height="14" rx="2"/><path d="M2.5 6.5 12 13l9.5-6.5" stroke="var(--plum)" stroke-width="2" fill="none"/></svg>
      </li>
      <li>www.glowformstudio.com
        <svg viewBox="0 0 24 24" fill="none" stroke="#fff" stroke-width="2"><circle cx="12" cy="12" r="10"/><ellipse cx="12" cy="12" rx="4.5" ry="10"/><path d="M2 12h20M4 7h16M4 17h16"/></svg>
      </li>
    </ul>
  </div>
</body>
</html>
```